New Logo design and Business cards

We are changing our business name and require a new Logo and business card design. Our new name will be "Brindlewood Garden Design & Construction" with a focus on enhancing our clients lifestyle through correct landscape design and construction of the designed landscape. We are a full service design to construct business meaning we take care of all aspects of designing and creating your ideal outdoor spaces. To see our current work and get a feel for what we do you can go to www.tarvogardens.com.au. We do not wish to have a major change to the website only the name/logo should change with all current colours etc being used in the new logo and business card. For our Logo I want the logo to reflect who we now are, and what we do, however I want it to have minimal impact on the website with the aim to only need to change the Logo and not colours or text styles. With the business card I need there to be a strong link between the card and the website with colours and looks being similar. I would love to see an image of one of our projects to be included on the card even as a backdrop. I have included a photo that I think could be used in the background of the business card. I have attached a copy of our current business cards (so you with have all relevant information required on the new cards) though I do want a fresh look with strong links to our website. Please feel free to contact me if you have any questions or ideas.

Brindlewood Garden Design & Construction-Shaping your weekends.

```html
<!DOCTYPE html>
<html lang="en">
<head>
<meta charset="utf-8">
<title>Brindlewood Garden Design &amp; Construction – Business Cards</title>
<link rel="stylesheet" href="https://fonts.googleapis.com/css2?family=Arimo:wght@400;700&display=swap">
<style>
  :root {
    --backdrop: #ebebeb;
    --coral: #f4846a;
    --purple: #b77fc9;
    --purple-deep: #9a5fb0;
    --ink: #0b0b0b;
    --paper: #ffffff;
    --grey-text: #6d6d6d;
    --peach: #f6cbb8;
    --photo-warm: #6b4a36;
    --photo-night: #2f3f63;
  }
  * { box-sizing: border-box; margin: 0; padding: 0; }
  html, body {
    width: 1200px; height: 1000px; overflow: hidden;
    background: var(--backdrop);
    font-family: "Arimo", Arial, sans-serif;
  }
  .sheet {
    position: relative; width: 1200px; height: 1000px;
    display: flex; align-items: center; justify-content: center; gap: 60px;
  }
  .card {
    position: relative; width: 520px; height: 318px; overflow: hidden;
    box-shadow: 0 10px 30px rgba(0,0,0,.18);
  }

  /* Front */
  .card--front { background: var(--paper); }
  .front__photo {
    position: absolute; right: 0; top: 0; width: 210px; height: 228px;
    background: linear-gradient(135deg, var(--photo-night) 0%, #7a5a44 45%, var(--photo-warm) 70%, #2c3a25 100%);
  }
  .front__photo-strip {
    position: absolute; left: 0; top: 0; width: 310px; height: 48px;
    background: linear-gradient(90deg, #d9d3cc 0%, var(--photo-night) 100%);
  }
  .brand {
    position: absolute; display: flex; align-items: center; gap: 10px;
  }
  .brand__mark { width: 30px; height: 30px; border-radius: 50%; flex: none; }
  .brand__name { font-weight: 400; letter-spacing: 1px; line-height: 1; white-space: nowrap; }
  .brand__sub { font-size: 10px; margin-top: 5px; white-space: nowrap; }
  .brand--front { left: 24px; top: 104px; }
  .brand--front .brand__mark { background: var(--peach); }
  .brand--front .brand__name { font-size: 25px; color: var(--purple-deep); }
  .brand--front .brand__sub { color: var(--grey-text); font-size: 10.5px; }

  .band {
    position: absolute; left: 0; right: 0; background: var(--ink);
  }
  .card--front .band { top: 228px; height: 72px; }
  .tagline {
    position: absolute; left: 22px; top: 24px; font-size: 22px;
  }
  .tagline__a { color: var(--purple); }
  .tagline__b { color: var(--paper); }
  .tagline__c { color: var(--coral); }
  .stripe {
    position: absolute; left: 0; right: 0; bottom: 0; height: 18px;
    background: var(--purple);
  }

  /* Back */
  .card--back { background: var(--coral); }
  .brand--back { left: 26px; top: 26px; }
  .brand--back .brand__mark { background: var(--paper); width: 26px; height: 26px; }
  .brand--back .brand__name { font-size: 26px; color: var(--paper); }
  .brand--back .brand__sub { color: var(--paper); }

  .contact {
    position: absolute; right: 24px; top: 86px; text-align: right; color: var(--paper);
  }
  .contact__name { font-size: 17px; font-weight: 700; letter-spacing: .5px; }
  .contact__role { font-size: 12px; margin-bottom: 18px; }
  .contact__line { font-size: 13px; line-height: 1.45; }
  .contact__label { font-weight: 700; }

  .card--back .band { top: 236px; height: 64px; }
  .services {
    position: absolute; left: 22px; top: 14px; color: var(--paper);
    font-size: 12.5px; line-height: 1.5;
  }
</style>
</head>
<body>
<main class="sheet">

  <section class="card card--front" aria-label="Business card front">
    <div class="front__photo" role="img" aria-label="Photograph of a lit outdoor living area with timber deck and garden at dusk"></div>
    <div class="front__photo-strip" role="img" aria-label="Photograph of an outdoor lounge with pool view at dusk"></div>
    <div class="brand brand--front">
      <span class="brand__mark"></span>
      <div>
        <div class="brand__name">BRINDLEWOOD</div>
        <div class="brand__sub">Garden Design &amp; Construction</div>
      </div>
    </div>
    <div class="band">
      <p class="tagline"><span class="tagline__a">Shaping</span> <span class="tagline__b">your</span> <span class="tagline__c">weekends</span></p>
    </div>
    <div class="stripe"></div>
  </section>

  <section class="card card--back" aria-label="Business card back">
    <div class="brand brand--back">
      <span class="brand__mark"></span>
      <div>
        <div class="brand__name">BRINDLEWOOD</div>
        <div class="brand__sub">Garden Design &amp; Construction</div>
      </div>
    </div>
    <div class="contact">
      <p class="contact__name">DANA HOLLIS</p>
      <p class="contact__role">Director</p>
      <p class="contact__line"><span class="contact__label">P:</span> 04 5550 1827</p>
      <p class="contact__line"><span class="contact__label">F:</span> 07 5550 3164</p>
      <p class="contact__line"><span class="contact__label">E:</span> dana@tarvogardens.com.au</p>
      <p class="contact__line">www.tarvogardens.com.au</p>
    </div>
    <div class="band">
      <p class="services">CAD Design incl. 3D • Structural Landscaping<br>Outdoor rooms, decks, gazebos • Excavation</p>
    </div>
    <div class="stripe"></div>
  </section>

</main>
</body>
</html>
```